Postcard design to acquire new clients for my Property Management Company

I'm looking for a postcard design that I can send to prospective clients detailing information about my company and services.
Postcard should be eye catching and contain information from www.brightkeyrentals-example.com. I've provided a few screen shots for the most important information and my logo.
Target Market(s)
Real Estate
Industry/Entity Type
Real Estate
Font styles to use
Sans Serif
Requirements
Must have
- Must be eye catching!! this will be a direct mail piece - I'd like for the card to be read and not tossed in the trash immediately.
Design que from the logo.
A place to write / print the receipts name and address.
our physical address - 2287 Marble Lane, Lubbock, TX 79555.
Should not have
- the contact information on the business card is not accurate - please use info from website.

```html
<!DOCTYPE html>
<html lang="en">
<head>
<meta charset="utf-8">
<title>BrightKey Rentals – Direct Mail Postcard</title>
<link rel="stylesheet" href="https://fonts.googleapis.com/css2?family=Montserrat:wght@600&family=Roboto+Condensed:wght@400;700&family=Roboto:wght@400;500;700&display=swap">
<style>
  :root{
    --navy:#0f3a68;
    --navy-deep:#0a2a4f;
    --steel:#8d9399;
    --steel-light:#c9cdd1;
    --paper:#ffffff;
    --paper-tint:#f1f3f5;
    --ink:#3d4248;
    --page:#e6e7e8;
  }
  *{box-sizing:border-box;margin:0;padding:0}
  html,body{width:1200px;height:860px;overflow:hidden;background:var(--page)}
  body{font-family:"Roboto",Arial,sans-serif;color:var(--ink);position:relative}

  .postcard{position:absolute;left:300px;width:600px;height:400px;background:var(--paper);overflow:hidden;box-shadow:0 6px 18px rgba(0,0,0,.18)}
  .postcard--front{top:20px}
  .postcard--back{top:440px}

  /* ---------- front ---------- */
  .brand-name{position:absolute;left:22px;top:26px;font-family:"Montserrat",Arial,sans-serif;font-weight:600;font-size:23px;letter-spacing:3px;color:var(--navy);text-transform:uppercase;line-height:1.15}
  .headline{position:absolute;left:0;top:94px;width:300px;height:64px;background:var(--navy);color:#fff;font-family:"Roboto Condensed",Arial,sans-serif;font-weight:700;font-size:21px;line-height:26px;padding:7px 0 0 16px;text-transform:uppercase}
  .tagline{position:absolute;left:16px;top:168px;width:260px;font-size:13px;line-height:17px;color:#5b6168}
  .photo-edge{position:absolute;left:268px;top:0;width:332px;height:216px;background:var(--steel);clip-path:polygon(46px 0,62px 0,16px 100%,0 100%)}
  .hero-photo{position:absolute;left:290px;top:12px;width:310px;height:204px;background:linear-gradient(135deg,#6f6a63 0%,#b9a58e 40%,#d8d2c8 65%,#4a4e55 100%);clip-path:polygon(42px 0,100% 0,100% 100%,0 100%)}

  .services{position:absolute;left:0;top:216px;width:600px;height:124px;background:linear-gradient(180deg,var(--navy) 0%,var(--navy-deep) 100%);display:grid;grid-template-columns:repeat(8,1fr);padding:10px 6px 0}
  .service{text-align:center;color:#fff;padding:0 3px}
  .service__icon{width:42px;height:42px;border:2px solid #fff;border-radius:50%;margin:0 auto 5px;display:flex;align-items:center;justify-content:center}
  .service__icon svg{width:20px;height:20px}
  .service__title{font-family:"Roboto Condensed",Arial,sans-serif;font-weight:700;font-size:7.8px;margin:0 -4px 3px;white-space:nowrap}
  .service__text{font-size:6.2px;line-height:7.6px;color:#d5dde8}

  .contact-strip{position:absolute;left:0;top:340px;width:600px;height:60px;background:var(--paper)}
  .contact-strip__grey{position:absolute;left:212px;top:0;width:388px;height:60px;background:var(--steel);clip-path:polygon(14px 0,100% 0,100% 100%,0 100%)}
  .contact-strip__rule{position:absolute;left:212px;top:0;width:20px;height:60px;background:var(--navy);clip-path:polygon(14px 0,18px 0,4px 100%,0 100%)}
  .phone{position:absolute;left:16px;top:16px;display:flex;align-items:center;gap:8px;font-family:"Roboto Condensed",Arial,sans-serif;font-weight:700;font-size:24px;color:var(--navy)}
  .phone svg{width:18px;height:22px}
  .contact-line{position:absolute;display:flex;align-items:center;gap:6px;color:#fff;font-size:11.5px}
  .contact-line svg{width:12px;height:12px}
  .contact-line--email{left:240px;top:12px}
  .contact-line--web{left:330px;top:36px}

  /* ---------- back ---------- */
  .back-brand{position:absolute;left:20px;top:18px;font-family:"Montserrat",Arial,sans-serif;font-weight:600;font-size:20px;letter-spacing:3px;color:var(--navy);text-transform:uppercase}
  .return-address{position:absolute;left:400px;top:20px;font-size:9.5px;line-height:13px;color:var(--ink)}
  .return-address strong{color:var(--navy);font-weight:700}
  .pricing-tab{position:absolute;left:18px;top:52px;background:var(--navy);color:#fff;font-family:"Roboto Condensed",Arial,sans-serif;font-weight:700;font-size:16px;letter-spacing:1px;padding:3px 30px 3px 10px;clip-path:polygon(0 0,88% 0,100% 100%,0 100%)}
  .plans{position:absolute;left:18px;top:78px;width:360px;display:grid;grid-template-columns:repeat(3,1fr);gap:6px}
  .plan{position:relative;background:var(--paper-tint);border-top:3px solid var(--navy);height:196px;padding:0 0 8px}
  .plan__name{background:var(--navy);color:#fff;font-family:"Roboto Condensed",Arial,sans-serif;font-weight:700;font-size:9.5px;text-align:center;padding:3px 0;text-transform:uppercase}
  .plan__flag{position:absolute;top:-14px;left:50%;transform:translateX(-50%);background:var(--steel);color:#fff;font-size:6px;padding:2px 8px;white-space:nowrap}
  .plan__rate{font-family:"Roboto Condensed",Arial,sans-serif;font-weight:700;font-size:26px;color:var(--navy);text-align:center;margin-top:8px;line-height:1}
  .plan__basis{font-size:6.5px;text-align:center;color:#6a7077;margin-bottom:8px}
  .plan__features{list-style:none;padding:0 5px}
  .plan__features li{font-size:6.2px;line-height:9.6px;padding-left:9px;position:relative;white-space:nowrap}
  .plan__features li::before{content:"";position:absolute;left:1px;top:2px;width:3px;height:5px;border:solid var(--navy);border-width:0 1.5px 1.5px 0;transform:rotate(40deg)}

  .cta-band{position:absolute;left:0;top:288px;width:430px;height:112px;background:var(--navy);clip-path:polygon(0 0,92% 0,100% 100%,0 100%)}
  .cta-band__headline{position:absolute;left:18px;top:298px;color:#fff;font-family:"Roboto Condensed",Arial,sans-serif;font-weight:700;font-size:13.5px;letter-spacing:.8px;text-transform:uppercase}
  .cta-band__bar{position:absolute;left:0;top:322px;width:370px;height:30px;background:var(--steel);clip-path:polygon(0 0,94% 0,100% 100%,0 100%)}
  .cta-band__contact{position:absolute;left:18px;top:326px;display:flex;align-items:center;gap:12px;color:#fff;font-family:"Roboto Condensed",Arial,sans-serif;font-weight:700;font-size:18px;text-transform:uppercase}
  .cta-band__contact svg{width:15px;height:18px}
  .cta-band__links{position:absolute;left:18px;top:364px;display:flex;gap:16px;color:#fff;font-size:10.5px}
  .cta-band__links span{display:flex;align-items:center;gap:5px}
  .cta-band__links svg{width:11px;height:11px}

  .address-block{position:absolute;left:400px;top:90px;width:180px}
  .address-block__line{height:1px;background:var(--steel-light);margin-bottom:34px}
</style>
</head>
<body>

<section class="postcard postcard--front" aria-label="Postcard front">
  <div class="brand-name">BrightKey<br>Rentals</div>
  <h1 class="headline">Property Management<br>Across Lubbock, TX</h1>
  <p class="tagline">Maximize your financial returns with support from our rental specialists</p>
  <div class="photo-edge"></div>
  <div class="hero-photo" role="img" aria-label="Photo of smiling homeowners shaking hands with a property manager across a desk"></div>

  <div class="services">
    <div class="service">
      <div class="service__icon"><svg viewBox="0 0 24 24" fill="#fff"><path d="M12 3 2 12h3v8h5v-5h4v5h5v-8h3z"/></svg></div>
      <div class="service__title">Property Marketing</div>
      <div class="service__text">Let us take over your marketing and find a qualified renter quickly.</div>
    </div>
    <div class="service">
      <div class="service__icon"><svg viewBox="0 0 24 24" fill="#fff"><circle cx="8" cy="8" r="3.5"/><circle cx="16" cy="8" r="3.5"/><path d="M1 20c0-4 3-7 7-7s7 3 7 7zM11 20c0-4 2-7 5-7 4 0 7 3 7 7z"/></svg></div>
      <div class="service__title">Tenant Screening</div>
      <div class="service__text">We screen all applications using fair housing guidelines to protect you.</div>
    </div>
    <div class="service">
      <div class="service__icon"><svg viewBox="0 0 24 24" fill="none" stroke="#fff" stroke-width="2.4" stroke-linecap="round"><path d="M12 2v20M17 6H9.5a3.5 3.5 0 0 0 0 7h5a3.5 3.5 0 0 1 0 7H6"/></svg></div>
      <div class="service__title">Rent Collection</div>
      <div class="service__text">We keep your tenants current and payments consistent.</div>
    </div>
    <div class="service">
      <div class="service__icon"><svg viewBox="0 0 24 24" fill="#fff"><path d="M13 3h6l2 3-4 1-2-1zM14 6l2 2-11 12-3-3z"/></svg></div>
      <div class="service__title">Maintenance</div>
      <div class="service__text">Let us coordinate repair work on your behalf.</div>
    </div>
    <div class="service">
      <div class="service__icon"><svg viewBox="0 0 24 24" fill="none" stroke="#fff" stroke-width="2.6" stroke-linecap="round"><circle cx="10" cy="10" r="6"/><path d="m15 15 6 6"/></svg></div>
      <div class="service__title">Property Inspections</div>
      <div class="service__text">We visit every home in our portfolio regularly with a proactive approach.</div>
    </div>
    <div class="service">
      <div class="service__icon"><svg viewBox="0 0 24 24" fill="none" stroke="#fff" stroke-width="2"><path d="M3 3v18h18"/><path d="M8 17v-5M12 17V8M16 17v-7M20 17V6" stroke-width="2.4"/></svg></div>
      <div class="service__title">Financial Reporting</div>
      <div class="service__text">We generate monthly statements so you can review income and expenses.</div>
    </div>
    <div class="service">
      <div class="service__icon"><svg viewBox="0 0 24 24" fill="#fff"><path d="M12 2 4 5v6c0 5 3.5 9 8 11 4.5-2 8-6 8-11V5z"/></svg></div>
      <div class="service__title">Evictions</div>
      <div class="service__text">We handle evictions for you and find new renters fast.</div>
    </div>
    <div class="service">
      <div class="service__icon"><svg viewBox="0 0 24 24" fill="none" stroke="#fff" stroke-width="2" stroke-linecap="round"><path d="M12 3v17M7 20h10M4 6h16M4 6l-3 7h6zM20 6l-3 7h6z"/></svg></div>
      <div class="service__title">Legal Guidance</div>
      <div class="service__text">Many ordinances and housing laws govern your relationship with tenants.</div>
    </div>
  </div>

  <div class="contact-strip">
    <div class="contact-strip__grey"></div>
    <div class="contact-strip__rule"></div>
    <div class="phone"><svg viewBox="0 0 18 22" fill="#0f3a68"><rect x="3" y="1" width="12" height="20" rx="2"/><rect x="5" y="4" width="8" height="12" fill="#fff"/></svg>(806) 555-0147</div>
    <div class="contact-line contact-line--email"><svg viewBox="0 0 12 12"><rect x="0" y="2" width="12" height="8" fill="#fff"/><path d="M0 2l6 5 6-5" fill="none" stroke="#8d9399"/></svg>info@brightkeyrentals-example.com</div>
    <div class="contact-line contact-line--web"><svg viewBox="0 0 12 12"><circle cx="6" cy="6" r="5.5" fill="#fff"/><circle cx="6" cy="6" r="3" fill="none" stroke="#8d9399"/></svg>www.brightkeyrentals-example.com</div>
  </div>
</section>

<section class="postcard postcard--back" aria-label="Postcard back">
  <div class="back-brand">BrightKey Rentals</div>
  <address class="return-address" style="font-style:normal"><strong>BrightKey Rentals</strong><br>2287 Marble Lane, Lubbock, TX 79555</address>
  <div class="pricing-tab">PRICING</div>

  <div class="plans">
    <div class="plan">
      <div class="plan__name">Lease Only</div>
      <div class="plan__rate">9%</div>
      <div class="plan__basis">of annual lease</div>
      <ul class="plan__features">
        <li>Professional Photography</li>
        <li>Marketing &amp; Advertising</li>
        <li>Property Showings</li>
        <li>Tenant Screening &amp; Qualifying</li>
        <li>Lease Execution</li>
        <li>Move In Coordination</li>
      </ul>
    </div>
    <div class="plan">
      <div class="plan__flag">Our Most Popular</div>
      <div class="plan__name">Full Service</div>
      <div class="plan__rate">10%</div>
      <div class="plan__basis">of monthly rent</div>
      <ul class="plan__features">
        <li>Includes Leasing Service</li>
        <li>24/7 Emergency Response</li>
        <li>Move In &amp; Out Inspections</li>
        <li>Professional Lease Enforcement</li>
        <li>Schedule &amp; Oversee all Repairs</li>
        <li>Pay all Invoices</li>
        <li>Monthly &amp; Year End Statements</li>
        <li>Annual Market Rent Analysis</li>
      </ul>
    </div>
    <div class="plan">
      <div class="plan__name">Premium Service</div>
      <div class="plan__rate">12%</div>
      <div class="plan__basis">of monthly rent</div>
      <ul class="plan__features">
        <li>Includes Full Service Features</li>
        <li>Professional Video Marketing</li>
        <li>Home Warranty Coordination</li>
        <li>Tenant Retention Program</li>
      </ul>
    </div>
  </div>

  <div class="address-block" aria-label="Recipient address">
    <div class="address-block__line"></div>
    <div class="address-block__line"></div>
    <div class="address-block__line"></div>
  </div>

  <div class="cta-band"></div>
  <div class="cta-band__headline">Choose the right property management system</div>
  <div class="cta-band__bar"></div>
  <div class="cta-band__contact">Contact Us <svg viewBox="0 0 18 22" fill="#fff"><rect x="3" y="1" width="12" height="20" rx="2"/><rect x="5" y="4" width="8" height="12" fill="#8d9399"/></svg> (806) 555-0147</div>
  <div class="cta-band__links">
    <span><svg viewBox="0 0 12 12"><rect x="0" y="2" width="12" height="8" fill="#fff"/><path d="M0 2l6 5 6-5" fill="none" stroke="#0f3a68"/></svg>info@brightkeyrentals-example.com</span>
    <span><svg viewBox="0 0 12 12"><circle cx="6" cy="6" r="5.5" fill="#fff"/><circle cx="6" cy="6" r="3" fill="none" stroke="#0f3a68"/></svg>www.brightkeyrentals-example.com</span>
  </div>
</section>

</body>
</html>
```